Keystone Prime Water Tank

I primarily market the water tanks so want a business care that reflects that. I have attached the water tank logo. You have been working on our water tank so maybe we can use that on the card et. I am leaving as one sided but can be double sided if that works. The information that needs to be on the cards is as follows: Gerald T. Munro Phone numbers: Office 555-284-9137 Direct 555-619-2405 Mobile 555-372-5841 email address: gerald@fieldgearworks.com Address P.O. Box 8273 Windermere, FL 30512 Web Page: www.fieldgearworks.com. A lot to fit on the card. Thanks

```html
<!DOCTYPE html>
<html lang="en">
<head>
<meta charset="utf-8">
<title>Keystone Prime Water Tank – Business Card</title>
<link href="https://fonts.googleapis.com/css2?family=Quicksand:wght@400;500;700&display=swap" rel="stylesheet">
<style>
  :root {
    --backdrop: #ece7de;
    --card: #232323;
    --card-pattern: #2a2a2a;
    --rule: #3a3a3a;
    --red: #f2333a;
    --white: #ffffff;
    --ink: #232323;
  }
  * { box-sizing: border-box; margin: 0; padding: 0; }
  html, body { width: 1200px; height: 800px; overflow: hidden; }
  body {
    background: var(--backdrop);
    font-family: "Quicksand", sans-serif;
    position: relative;
  }
  .card {
    position: absolute;
    top: 151px;
    width: 286px;
    height: 500px;
    background: var(--card);
    color: var(--white);
  }
  .card--front { left: 244px; }
  .card--back { left: 659px; }

  .brand {
    position: absolute;
    display: flex;
    flex-direction: column;
    align-items: center;
    gap: 12px;
  }
  .brand__mark { width: 44px; height: 44px; background: var(--red); }
  .brand__name {
    font-weight: 700;
    font-size: 18px;
    line-height: 20px;
    text-transform: uppercase;
    text-align: center;
    letter-spacing: 0.5px;
    color: var(--white);
  }
  .card--front .brand { left: 0; right: 0; top: 34px; }

  .person { position: absolute; left: 0; right: 0; top: 164px; text-align: center; }
  .person__name { font-weight: 500; font-size: 24px; line-height: 26px; }
  .person__title { font-weight: 500; font-size: 23px; line-height: 24px; color: var(--red); }

  .contacts { position: absolute; left: 22px; right: 21px; top: 246px; list-style: none; }
  .contact {
    position: relative;
    height: 41px;
    border-top: 1px solid var(--rule);
    text-align: center;
    font-size: 13.5px;
    line-height: 17px;
    font-weight: 400;
    padding-top: 11px;
    white-space: nowrap;
  }
  .contact__icon {
    position: absolute;
    left: 50%;
    top: -9px;
    width: 21px;
    height: 19px;
    margin-left: -10.5px;
  }

  .pattern { position: absolute; inset: 0; background: linear-gradient(160deg, var(--card-pattern), var(--card)); }
  .card--back .brand { right: 19px; bottom: 31px; align-items: flex-end; }
  .card--back .brand__name { text-align: right; }
</style>
</head>
<body>
  <section class="card card--front">
    <div class="brand">
      <span class="brand__mark"></span>
      <span class="brand__name">Keystone Prime<br>Water Tank</span>
    </div>

    <div class="person">
      <p class="person__name">Gerald t. munro</p>
      <p class="person__title">president</p>
    </div>

    <ul class="contacts">
      <li class="contact">
        <svg class="contact__icon" viewBox="0 0 21 19"><path d="M10.5 0 21 19H0z" fill="var(--red)"/><path d="M8 9.5c.6 2 1.7 3.2 3.7 3.9l1-1 1.4.8-.6 1.2c-3 0-5.6-2.6-5.8-5.6l1.2-.6.8 1.4z" fill="var(--ink)"/></svg>
        555-284-9137
      </li>
      <li class="contact">
        <svg class="contact__icon" viewBox="0 0 21 19"><path d="M10.5 0 21 19H0z" fill="var(--red)"/><path d="M8 9.5c.6 2 1.7 3.2 3.7 3.9l1-1 1.4.8-.6 1.2c-3 0-5.6-2.6-5.8-5.6l1.2-.6.8 1.4z" fill="var(--ink)"/></svg>
        555-619-2405
      </li>
      <li class="contact">
        <svg class="contact__icon" viewBox="0 0 21 19"><path d="M10.5 0 21 19H0z" fill="var(--red)"/><rect x="8.8" y="8" width="3.4" height="6.5" rx=".6" fill="none" stroke="var(--ink)" stroke-width=".9"/></svg>
        555-372-5841
      </li>
      <li class="contact">
        <svg class="contact__icon" viewBox="0 0 21 19"><path d="M10.5 0 21 19H0z" fill="var(--red)"/><path d="M10.5 15s-2.4-2.8-2.4-4.4a2.4 2.4 0 0 1 4.8 0c0 1.6-2.4 4.4-2.4 4.4z" fill="var(--ink)"/><circle cx="10.5" cy="10.6" r=".8" fill="var(--red)"/></svg>
        8273 cedarvale, ga 30512
      </li>
      <li class="contact">
        <svg class="contact__icon" viewBox="0 0 21 19"><path d="M10.5 0 21 19H0z" fill="var(--red)"/><circle cx="10.5" cy="11.5" r="2.8" fill="none" stroke="var(--ink)" stroke-width=".8"/><path d="M7.7 11.5h5.6M10.5 8.7v5.6" stroke="var(--ink)" stroke-width=".7"/></svg>
        www.fieldgearworks.com
      </li>
      <li class="contact">
        <svg class="contact__icon" viewBox="0 0 21 19"><path d="M10.5 0 21 19H0z" fill="var(--red)"/><rect x="7.6" y="9.6" width="5.8" height="4" fill="var(--ink)"/><path d="M7.6 9.6l2.9 2.2 2.9-2.2" fill="none" stroke="var(--red)" stroke-width=".6"/></svg>
        gerald@fieldgearworks.com
      </li>
    </ul>
  </section>

  <section class="card card--back">
    <div class="pattern" role="img" aria-label="Faint repeating brand symbol pattern across the card back"></div>
    <div class="brand">
      <span class="brand__mark"></span>
      <span class="brand__name">Keystone Prime<br>Water Tank</span>
    </div>
  </section>
</body>
</html>
```